design a construction company business card

Design business card around our logo. Card must have all the typical info: name, title, address, phone, email, business name, etc. Somewhere on the card I would like to see our motto "Crafted with care... Driven by dedication." Consider adding a splash of bright orange to the card to complement the blues and silvers/grays in the logo. We are open to metallic inks, textures, etc. We would like to see options on both light and dark backgrounds. The font in the logo is Euro Technic Extended Regular.

```html
<!DOCTYPE html>
<html lang="en">
<head>
<meta charset="utf-8">
<title>Harlan Building Co. – Business Card</title>
<link rel="stylesheet" href="https://fonts.googleapis.com/css2?family=Jost:ital,wght@0,300;0,400;0,600;0,700;1,400&display=swap">
<style>
  :root {
    --blue: #1547f2;
    --blue-deep: #0a1ef0;
    --blue-light: #2f8cff;
    --silver: #d9dcdc;
    --silver-soft: #eceeee;
    --paper: #ffffff;
    --paper-shade: #e9e9e9;
    --ink: #3d4147;
    --motto: #c9c9c9;
  }
  * { margin: 0; padding: 0; box-sizing: border-box; }
  html, body { width: 1022px; height: 1200px; overflow: hidden; background: var(--paper); }
  body { position: relative; font-family: "Jost", sans-serif; color: var(--ink); }

  .card { position: absolute; border-radius: 70px; overflow: hidden; }
  .card svg.card-art { position: absolute; inset: 0; width: 100%; height: 100%; display: block; }
  .card-front { left: 59px; top: 39px; width: 918px; height: 520px; }
  .card-back  { left: 45px; top: 638px; width: 932px; height: 529px; }

  .motto {
    position: absolute; top: 14px; left: 0; width: 100%; text-align: center;
    font-weight: 700; font-size: 24px; letter-spacing: 3.6px; color: var(--motto);
    text-transform: uppercase; white-space: nowrap;
  }

  .wordmark {
    position: absolute; transform: translate(-50%, -50%); text-align: center;
    font-weight: 700; color: var(--blue); line-height: 1; white-space: nowrap;
  }
  .wordmark .name { display: block; font-size: 70px; letter-spacing: 6px; }
  .wordmark .sub  { display: block; font-size: 24px; letter-spacing: 5px; margin-top: 8px; }
  .card-front .wordmark { left: 458px; top: 225px; }
  .card-back .wordmark { left: 741px; top: 300px; color: var(--paper); }
  .card-back .wordmark .name { font-size: 58px; letter-spacing: 5px; }
  .card-back .wordmark .sub  { font-size: 20px; letter-spacing: 4px; }

  .person { position: absolute; left: 55px; top: 22px; }
  .person-name { font-size: 56px; line-height: 1; color: var(--blue); letter-spacing: -1px; }
  .person-name .first { font-weight: 300; }
  .person-name .last { font-weight: 700; }
  .person-title { font-style: italic; font-size: 23px; margin-top: 8px; color: var(--ink); }

  .contact { position: absolute; right: 560px; text-align: right; font-size: 23px; line-height: 29px; color: var(--ink); white-space: nowrap; }
  .contact-phone { top: 175px; }
  .contact-email { top: 255px; }
  .contact-address { top: 308px; }
  .icon { position: absolute; left: 390px; width: 38px; height: 38px; }
  .icon-phone { top: 172px; }
  .icon-email { top: 252px; }
  .icon-pin { top: 315px; }
</style>
</head>
<body>

<section class="card card-front">
  <svg class="card-art" viewBox="0 0 1050 595" preserveAspectRatio="none" aria-hidden="true">
    <defs>
      <radialGradient id="paperFront" cx="0.5" cy="0.45" r="0.7">
        <stop offset="0.45" stop-color="#ffffff"/>
        <stop offset="1" stop-color="#e6e6e6"/>
      </radialGradient>
      <linearGradient id="blueWave" x1="0" y1="0" x2="1" y2="0">
        <stop offset="0" stop-color="#2a7dff"/>
        <stop offset="0.5" stop-color="#1d56f5"/>
        <stop offset="1" stop-color="#0a1ef0"/>
      </linearGradient>
      <linearGradient id="blueCorner" x1="0" y1="1" x2="1" y2="0">
        <stop offset="0" stop-color="#33a4ff"/>
        <stop offset="0.5" stop-color="#1a4ff3"/>
        <stop offset="1" stop-color="#0a1ef0"/>
      </linearGradient>
    </defs>
    <rect width="1050" height="595" fill="url(#paperFront)"/>
    <path d="M0,215 C60,360 300,420 560,365 C300,425 90,390 0,305 Z" fill="var(--silver)"/>
    <path d="M0,373 C150,460 350,450 560,390 C700,350 820,335 900,333 C760,380 620,480 542,595 L0,595 Z" fill="url(#blueWave)"/>
    <path d="M930,345 C800,400 650,500 575,595 L645,595 C705,500 820,410 930,345 Z" fill="var(--silver)"/>
    <path d="M1050,315 C900,380 760,490 687,595 L1050,595 Z" fill="url(#blueCorner)"/>
  </svg>
  <p class="motto">Crafted with care...driven by dedication</p>
  <div class="wordmark"><span class="name">HARLAN</span><span class="sub">BUILDING CO.</span></div>
</section>

<section class="card card-back">
  <svg class="card-art" viewBox="0 0 1066 605" preserveAspectRatio="none" aria-hidden="true">
    <defs>
      <radialGradient id="paperBack" cx="0.3" cy="0.45" r="0.7">
        <stop offset="0.45" stop-color="#ffffff"/>
        <stop offset="1" stop-color="#e6e6e6"/>
      </radialGradient>
      <linearGradient id="blueBack" x1="0" y1="1" x2="1" y2="0">
        <stop offset="0" stop-color="#2f8cff"/>
        <stop offset="0.45" stop-color="#1a4ff3"/>
        <stop offset="1" stop-color="#0a1ef0"/>
      </linearGradient>
    </defs>
    <rect width="1066" height="605" fill="url(#paperBack)"/>
    <path d="M612,250 C600,420 450,560 225,605 L300,605 C485,540 625,420 612,250 Z" fill="var(--silver)"/>
    <path d="M596,0 L1066,0 L1066,605 L398,605 C560,500 660,330 596,0 Z" fill="url(#blueBack)"/>
  </svg>

  <div class="person">
    <h1 class="person-name"><span class="first">DALE</span><span class="last">HARLAN</span></h1>
    <p class="person-title">President</p>
  </div>

  <p class="contact contact-phone">513-555-0147</p>
  <p class="contact contact-email">info@harlanbuildingco.com</p>
  <p class="contact contact-address">2740 Birchwood Lane<br>Springfield, OH 45502</p>

  <svg class="icon icon-phone" viewBox="0 0 38 38" aria-hidden="true">
    <circle cx="19" cy="19" r="19" fill="var(--blue)"/>
    <path d="M13 10 l4 0 l1.5 5 l-2.5 2 c1.2 2.6 3 4.4 5.5 5.5 l2-2.5 l5 1.5 l0 4 c-10 1 -16.5 -6 -15.5 -15.5 Z" fill="#fff"/>
  </svg>
  <svg class="icon icon-email" viewBox="0 0 38 38" aria-hidden="true">
    <rect x="0" y="6" width="38" height="26" rx="2" fill="var(--blue)"/>
    <path d="M1 8 L19 21 L37 8" fill="none" stroke="#fff" stroke-width="2.5"/>
  </svg>
  <svg class="icon icon-pin" viewBox="0 0 38 38" aria-hidden="true">
    <path d="M19 2 C11 2 7 8 7 13.5 C7 22 19 36 19 36 C19 36 31 22 31 13.5 C31 8 27 2 19 2 Z" fill="var(--blue)"/>
    <circle cx="19" cy="14" r="4.5" fill="#fff"/>
  </svg>

  <div class="wordmark"><span class="name">HARLAN</span><span class="sub">BUILDING CO.</span></div>
</section>

</body>
</html>
```